New Brand - Website Design (4 Pages)

We are launching a new brand for electronic cigarettes. We already have logo and packaging done and would like a web design to go with it.

We are interested in the following deliverables:

1) Home Page Design
2) Check Out Design
3) How it Works Page
4) Secondary Template Page Design

Looking for a 60s modern look and something that is consistent with our logo and packaging.

Industry/Entity Type

Electronic

Requirements
Must have
• Consistent with logo and packaging (Use Logo Attached)
White background

Example (Functionality & Design): http://www.torvex.co.uk/
Example (Design): http://www.quillharbor.com/

We want the design more like quillharbor but the functionality the same as torvex.

Top Bar: Pebble Arcs Kits; Cartridge Refills; How it Works; Contact; My Account; Checkout
Should not have
• Stock List or Search Bar or Newsletter Signup

```html
<!DOCTYPE html>
<html lang="en">
<head>
<meta charset="utf-8">
<title>How It Works – Pebble Arcs</title>
<link rel="stylesheet" href="https://fonts.googleapis.com/css2?family=Didact+Gothic&family=Poiret+One&family=Open+Sans&family=Oswald:wght@500&display=swap">
<style>
  :root {
    --page-bg: #ececec;
    --ink: #1f1f1f;
    --panel: #222222;
    --panel-text: #ffffff;
    --body-grey: #6e6e6e;
    --heading-grey: #333333;
    --accent: #8fd3f4;
    --timeline: #222222;
  }
  * { margin: 0; padding: 0; box-sizing: border-box; }
  html, body { width: 1200px; height: 1000px; overflow: hidden; }
  body {
    position: relative;
    background: linear-gradient(180deg, #efefef 0%, var(--page-bg) 100%);
    font-family: "Didact Gothic", sans-serif;
    color: var(--ink);
  }
  .site-header { position: absolute; inset: 0 0 auto 0; height: 100px; }
  .nav-dot {
    position: absolute; left: 150px; top: 41px;
    width: 31px; height: 31px; border-radius: 50%;
    background: var(--accent);
  }
  .main-nav a {
    position: absolute; top: 50px;
    font-size: 11.5px; letter-spacing: 0.3px; font-weight: 700;
    color: #111; text-decoration: none; text-transform: uppercase;
  }
  .main-nav a.is-current::after {
    content: ""; position: absolute; left: -7px; right: -7px; top: 16px;
    height: 4px; background: var(--accent);
  }
  .brand {
    position: absolute; left: 910px; top: 24px;
    display: flex; align-items: center; gap: 10px;
  }
  .brand-circle { width: 52px; height: 52px; border-radius: 50%; background: var(--accent); }
  .brand-name { font-size: 20px; color: var(--ink); letter-spacing: 1px; text-transform: uppercase; line-height: 1; }

  .intro-panel {
    position: absolute; left: 146px; top: 102px; width: 906px; height: 226px;
    background: var(--panel); color: var(--panel-text);
    padding: 10px 20px 0 20px;
  }
  .intro-title { font-family: "Poiret One", sans-serif; font-size: 41px; font-weight: 400; line-height: 1.05; }
  .intro-text { font-family: "Open Sans", sans-serif; font-size: 17.3px; line-height: 25.7px; margin-top: 0; }

  .timeline-line {
    position: absolute; left: 167px; top: 440px; width: 14px; height: 600px;
    background: var(--timeline);
  }
  .step-marker {
    position: absolute; left: 141px; width: 66px; height: 66px; border-radius: 50%;
    background: var(--timeline); color: #fff;
    font-family: "Oswald", sans-serif; font-size: 22px;
    display: flex; align-items: center; justify-content: center;
  }
  .step { position: absolute; left: 236px; width: 880px; }
  .step-title { font-family: "Poiret One", sans-serif; font-weight: 400; font-size: 29px; letter-spacing: 0.5px; color: var(--heading-grey); line-height: 1; }
  .step-text {
    font-family: "Poiret One", sans-serif; font-weight: 700; font-size: 19px;
    letter-spacing: 0.7px; line-height: 25.5px; color: var(--body-grey);
    margin-top: 16px; white-space: nowrap;
  }
</style>
</head>
<body>
  <header class="site-header">
    <span class="nav-dot"></span>
    <nav class="main-nav">
      <a href="#" style="left:198px">Catridge Refills</a>
      <a href="#" class="is-current" style="left:325px">How it works</a>
      <a href="#" style="left:450px">My Account</a>
      <a href="#" style="left:575px">Check out</a>
      <a href="#" style="left:668px">One Year Warranty</a>
      <a href="#" style="left:822px">Contact</a>
    </nav>
    <div class="brand">
      <span class="brand-circle"></span>
      <span class="brand-name">Pebble Arcs</span>
    </div>
  </header>

  <section class="intro-panel">
    <h1 class="intro-title">HOW IT WORKS</h1>
    <p class="intro-text">Proin gravida nibh vel velit auctor aliquet. Aenean sollicitudin, lorem quis bibendum auctor, nisi elit conse-quat ipsum, nec sagittis sem nibh id elit. Duis sed odio sit amet nibh vulputate cursus a sit amet mauris. Morbi accumsan ipsum velit. Nam nec tellus a odio tincidunt auctor a ornare odio. Sed non &nbsp;mauris vitae erat consequat auctor eu in elit. Class aptent taciti sociosqu ad litora torquent per conubia nostra, per inceptos himenaeos. Mauris in erat justo. Nullam ac urna eu felis dapibus condimentum sit amet a augue. Sed non neque elit. Sed ut</p>
  </section>

  <div class="timeline-line"></div>
  <span class="step-marker" style="top:408px">1</span>
  <span class="step-marker" style="top:597px">2</span>
  <span class="step-marker" style="top:782px">3</span>
  <span class="step-marker" style="top:967px">4</span>

  <article class="step" style="top:373px">
    <h2 class="step-title">HOW WORKS 1</h2>
    <p class="step-text">This is Inkstudio's version &nbsp;of Lorem Ipsum. Proin gravida nibh vel velit auctor aliquet. Aenean<br>sollicitudin, lorem quis bibendum auctor, nisi elit consequat ipsum, nec sagittis sem nibh id elit.<br>Duis sed odio sit amet nibh vulputate cursus a sit amet mauris. Morbi accumsan ipsum velit. Nam<br>nec tellus a odio tincidunt auctor a ornare odio. Sed non &nbsp;mauris vitae erat consequat auctor</p>
  </article>
  <article class="step" style="top:550px">
    <h2 class="step-title">HOW WORKS 2</h2>
    <p class="step-text">This is Inkstudio's version &nbsp;of Lorem Ipsum. Proin gravida nibh vel velit auctor aliquet. Aenean<br>sollicitudin, lorem quis bibendum auctor, nisi elit consequat ipsum, nec sagittis sem nibh id elit.<br>Duis sed odio sit amet nibh vulputate cursus a sit amet mauris. Morbi accumsan ipsum velit. Nam<br>nec tellus a odio tincidunt auctor a ornare odio. Sed non &nbsp;mauris vitae erat consequat auctor</p>
  </article>
  <article class="step" style="top:733px">
    <h2 class="step-title">HOW WORKS 3</h2>
    <p class="step-text">This is Inkstudio's version &nbsp;of Lorem Ipsum. Proin gravida nibh vel velit auctor aliquet. Aenean<br>sollicitudin, lorem quis bibendum auctor, nisi elit consequat ipsum, nec sagittis sem nibh id elit.<br>Duis sed odio sit amet nibh vulputate cursus a sit amet mauris. Morbi accumsan ipsum velit. Nam<br>nec tellus a odio tincidunt auctor a ornare odio. Sed non &nbsp;mauris vitae erat consequat auctor</p>
  </article>
  <article class="step" style="top:923px">
    <h2 class="step-title">HOW WORKS 4</h2>
    <p class="step-text">This is Inkstudio's version &nbsp;of Lorem Ipsum. Proin gravida nibh vel velit auctor aliquet. Aenean<br>sollicitudin, lorem quis bibendum auctor, nisi elit consequat ipsum, nec sagittis sem nibh id elit.</p>
  </article>
</body>
</html>
```